Visitenkarten-Design für Fotograf gesucht
Zielgruppe
Ich bin Fotograf der ein step in Richtung Professionalität wagen möchte.
Aufgabenstellung
Ich habe bereits ein Logo welches ich als Datei angefügt habe.
Ich hatte überlegt gehabt eine Art Prägung im Design zu haben bzw. in der Visitenkarte, eventuell das Kamera Zeichen in meinem Logo. Sonst bin ich relativ offen.
Eine weitere Überlegung ist eine eher kontrastreiche Karte haben könnte, eventuell die Rückseite dunkelgrau oder schwarz.
Es kann wenn man eine dritte Farbe hinzufügen möchte ein mittleres bis dunkles Rot hinzufügen.
Ich habe ein paar Designs hinzugefügt die mir sehr zugesagt haben.
Ansonsten bin ich auch für ein Design in der kompletten Gegenteiligkeit offen.

```html
<!DOCTYPE html>
<html lang="de">
<head>
<meta charset="utf-8">
<title>Mirko Trell – Visitenkarte</title>
<link rel="stylesheet" href="https://fonts.googleapis.com/css2?family=Open+Sans:wght@400;600;700&display=swap">
<style>
  :root {
    --stage: #2e2e2f;
    --paper: #f3f3f3;
    --ink: #222222;
    --ink-soft: #3a3a3a;
    --faint: #d9d9d9;
    --grey-art: #bdbdbd;
    --red: #d7141a;
  }
  * { box-sizing: border-box; margin: 0; padding: 0; }
  html, body {
    width: 1200px; height: 800px; overflow: hidden;
    background: var(--stage);
    font-family: "Open Sans", Arial, sans-serif;
  }
  .sheet {
    width: 1200px; height: 800px;
    display: flex; align-items: center; justify-content: center; gap: 40px;
  }
  .card {
    position: relative; width: 540px; height: 350px;
    background: var(--paper); overflow: hidden;
    box-shadow: 0 10px 30px rgba(0,0,0,.45);
  }
  /* stripes */
  .stripe-band { position: absolute; left: 0; bottom: 26px; width: 270px; height: 12px; }
  .stripe-lines { position: absolute; right: 0; bottom: 28px; width: 240px; height: 12px; }

  /* contact side */
  .faint-name {
    position: absolute; left: 170px; top: 62px;
    font-size: 54px; font-weight: 400; color: var(--faint); letter-spacing: 1px;
    white-space: nowrap;
  }
  .identity { position: absolute; left: 40px; top: 58px; }
  .identity .name { font-size: 24px; font-weight: 700; color: var(--red); }
  .identity .role { font-size: 14px; color: var(--ink-soft); margin-top: 4px; }
  .address {
    position: absolute; left: 330px; top: 170px;
    display: flex; gap: 10px; font-size: 14px; color: var(--ink); line-height: 1.5;
  }
  .contact-list { position: absolute; left: 40px; top: 200px; list-style: none; }
  .contact-list li {
    display: flex; align-items: center; gap: 18px;
    font-size: 14px; color: var(--ink); height: 24px;
  }
  .icon { width: 16px; height: 16px; flex: none; }

  /* logo side */
  .camera-art {
    position: absolute; left: 0; top: 0; width: 130px; height: 312px;
    background: linear-gradient(90deg, #c9c9c9, var(--grey-art) 60%, #d8d8d8);
  }
  .wordmark {
    position: absolute; left: 190px; top: 132px;
    display: flex; align-items: center; gap: 14px;
  }
  .wordmark .label { font-size: 34px; font-weight: 400; color: var(--ink); white-space: nowrap; line-height: 1; }
  .wordmark .mark { width: 16px; height: 16px; background: var(--ink); flex: none; }
</style>
</head>
<body>
<main class="sheet">

  <section class="card card-contact">
    <div class="faint-name" aria-hidden="true">Mirko Trell</div>
    <div class="identity">
      <div class="name">Mirko Trell</div>
      <div class="role">Fotograf</div>
    </div>

    <div class="address">
      <svg class="icon" viewBox="0 0 16 16" aria-hidden="true">
        <path d="M8 1a5 5 0 0 0-5 5c0 3.6 5 9 5 9s5-5.4 5-9a5 5 0 0 0-5-5z" fill="#222"/>
        <circle cx="8" cy="6" r="1.8" fill="#f3f3f3"/>
      </svg>
      <div>lindenweg 12<br>34567 beispielstadt</div>
    </div>

    <ul class="contact-list">
      <li>
        <svg class="icon" viewBox="0 0 16 16" aria-hidden="true">
          <path d="M4 1.5l2.5 3-1.5 1.5c.8 2 2.5 3.7 4.5 4.5l1.5-1.5 3 2.5-1.5 2.5C7 14 2 9 1.5 3z" fill="#222"/>
        </svg>
        +49 321 654 987
      </li>
      <li>
        <svg class="icon" viewBox="0 0 16 16" aria-hidden="true">
          <rect x="1" y="3" width="14" height="10" fill="#222"/>
          <path d="M1.5 3.5L8 9l6.5-5.5" stroke="#f3f3f3" stroke-width="1.2" fill="none"/>
        </svg>
        info@mt-studio.de
      </li>
      <li>
        <svg class="icon" viewBox="0 0 16 16" aria-hidden="true">
          <circle cx="8" cy="8" r="6.5" fill="#222"/>
          <path d="M1.5 8h13M8 1.5c-3 3.5-3 9.5 0 13M8 1.5c3 3.5 3 9.5 0 13" stroke="#f3f3f3" stroke-width="1" fill="none"/>
        </svg>
        www.mt-studio.de
      </li>
    </ul>

    <svg class="stripe-band" viewBox="0 0 270 12" preserveAspectRatio="none" aria-hidden="true">
      <polygon points="0,0 270,0 258,12 0,12" fill="#d7141a"/>
    </svg>
    <svg class="stripe-lines" viewBox="0 0 240 12" preserveAspectRatio="none" aria-hidden="true">
      <polygon points="4,0 240,0 240,4 0,4" fill="#d7141a"/>
      <rect x="0" y="8" width="240" height="2" fill="#d7141a"/>
    </svg>
  </section>

  <section class="card card-logo">
    <div class="camera-art" role="img" aria-label="Grau gehaltene Illustration einer klassischen zweiäugigen Kamera, am linken Rand angeschnitten"></div>
    <div class="wordmark">
      <span class="label">Mirko Trell</span>
      <span class="mark" aria-hidden="true"></span>
    </div>
    <svg class="stripe-band" viewBox="0 0 270 12" preserveAspectRatio="none" aria-hidden="true">
      <polygon points="0,0 270,0 258,12 0,12" fill="#d7141a"/>
    </svg>
    <svg class="stripe-lines" viewBox="0 0 240 12" preserveAspectRatio="none" aria-hidden="true">
      <polygon points="4,0 240,0 240,4 0,4" fill="#d7141a"/>
      <rect x="0" y="8" width="240" height="2" fill="#d7141a"/>
    </svg>
  </section>

</main>
</body>
</html>
```